FinTech company looking to revamp and expand client-facing interface for our financial models

Halvern Ledgerworks currently has a very simple website that allows clients to interact with our financial models. We are looking to completely redesign the current site and add several extra pages to provide extra functionality. We want the design to have a modern, slick feel, that will work on both a desktop or a tablet. It should be straightforward for clients to move between different pages at any time, and clear from the layout how to interact with the more advanced features. We have included screenshots of existing pages in the attached design brief, as well as sketches of the functionality required by the new pages, but can't provide a direct link to the current site.
Target Market(s)
Professional investors that will be paying to access the interface
Industry/Entity Type
Finance
Number of Pages Required
4 page
Colors
Designer to choose colors to be used in the design.
Look and feel
Each slider illustrates characteristics of the customer's brand and the style your logo design should communicate.

```html
<!DOCTYPE html>
<html lang="en">
<head>
<meta charset="utf-8">
<title>Halvern Ledgerworks — Models</title>
<link href="https://fonts.googleapis.com/css2?family=Roboto:wght@300;400;500&display=swap" rel="stylesheet">
<style>
:root{
  --page:#f5f7fa;
  --white:#ffffff;
  --brand:#2b8be0;
  --panel:#1864a8;
  --panel-line:#6fa4d4;
  --ink:#2e3338;
  --muted:#8d96a0;
  --faint:#c3cad3;
  --row-alt:#f3f7fb;
  --star:#e8473f;
}
*{box-sizing:border-box;margin:0;padding:0}
html,body{width:1200px;height:676px;overflow:hidden}
body{background:var(--page);font-family:'Roboto',sans-serif;color:var(--ink);position:relative}
.topbar{position:absolute;left:0;top:0;width:1200px;height:67px;background:var(--white);box-shadow:0 2px 8px rgba(0,0,0,.04)}
.brand-name{position:absolute;left:150px;top:19px;font-size:22px;font-weight:400;letter-spacing:.5px;color:#2a2f35}
.horizon{position:absolute;top:0;height:67px;line-height:67px;font-size:12.5px;color:var(--ink);text-align:center}
.horizon.active{background:var(--brand);color:var(--white)}
.nav-item{position:absolute;top:0;height:67px;display:flex;align-items:center;gap:7px;font-size:13px;color:var(--ink)}
.nav-item svg{width:17px;height:17px}
.nav-item.active{color:var(--brand);border-bottom:2px solid var(--brand);padding:0 15px}

.filter{position:absolute;left:0;top:118px;width:315px;height:285px;background:var(--panel);color:var(--white);box-shadow:0 4px 12px rgba(0,0,0,.12)}
.filter-title{position:absolute;left:11px;top:17px;display:flex;align-items:center;gap:8px;font-size:13.5px;font-weight:500}
.dark-toggle{position:absolute;left:206px;top:11px;width:94px;height:27px;border:1px solid #163a5c;border-radius:14px;display:flex;align-items:center;justify-content:center;gap:4px;font-size:11px;color:#1b2c3e}
.f-label{position:absolute;left:33px;font-size:14px;font-weight:500}
.f-text{position:absolute;font-size:12.5px}
.f-input{position:absolute;height:30px;border:1px solid var(--panel-line);font-size:10.5px;color:#9ec3e6;padding:0 6px;line-height:28px;font-weight:300;white-space:nowrap;overflow:hidden;letter-spacing:-.1px}
.cal{position:absolute;width:12px;height:12px}
.cancel{position:absolute;left:181px;top:251px;font-size:12.5px;color:#6e9fcc}
.apply{position:absolute;left:232px;top:246px;width:68px;height:27px;border-radius:14px;background:var(--white);color:var(--brand);font-size:12.5px;text-align:center;line-height:27px}

.asset-tab{position:absolute;top:118px;height:27px;line-height:27px;font-size:12px;color:var(--faint);white-space:nowrap}
.asset-tab.active{background:var(--brand);color:var(--white);border-radius:14px;width:83px;text-align:center}
.popout{position:absolute;left:1184px;top:123px;width:13px;height:13px}

.models{position:absolute;left:337px;top:156px;width:863px;height:464px;overflow:hidden;background:var(--white);border-radius:4px 0 0 4px}
.row{display:grid;grid-template-columns:92px 82px 89px 80px 70px 68px 69px 74px 72px 69px 68px 80px;align-items:center;white-space:nowrap;font-size:12.5px}
.row.head{height:45px;background:var(--row-alt);color:var(--muted)}
.row.body{height:70px}
.row.body:nth-child(odd){background:var(--row-alt)}
.id-cell{padding-left:14px;display:flex;align-items:center;gap:6px}
.head .id-cell{padding-left:14px;gap:5px}
.star{width:9px;height:9px}
.time{line-height:1.28}
</style>
</head>
<body>
<header class="topbar">
  <div class="brand-name">LEDGRA</div>
  <div class="horizon active" style="left:262px;width:60px">250D</div>
  <div class="horizon" style="left:340px">83D</div>
  <div class="horizon" style="left:398px">42D</div>
  <nav>
    <div class="nav-item active" style="left:538px">
      <svg viewBox="0 0 24 24" fill="none" stroke="currentColor" stroke-width="1.8"><path d="M3 11 12 3l9 8M5 9.5V21h14V9.5"/></svg>Models
    </div>
    <div class="nav-item" style="left:657px">
      <svg viewBox="0 0 24 24" fill="none" stroke="currentColor" stroke-width="1.8"><circle cx="5" cy="5" r="2"/><circle cx="12" cy="5" r="2"/><circle cx="19" cy="5" r="2"/><circle cx="5" cy="12" r="2"/><circle cx="12" cy="12" r="2"/><circle cx="19" cy="12" r="2"/><circle cx="12" cy="19" r="2"/></svg>Portfolio Builder
    </div>
    <div class="nav-item" style="left:816px">
      <svg viewBox="0 0 24 24" fill="none" stroke="currentColor" stroke-width="1.8"><path d="M12 3 2 8l10 5 10-5-10-5zM2 13l10 5 10-5"/></svg>Sensitivities
    </div>
    <div class="nav-item" style="left:953px">
      <svg viewBox="0 0 24 24" fill="none" stroke="currentColor" stroke-width="1.8"><path d="m12 2.8 2.8 6 6.5.7-4.9 4.4 1.4 6.4L12 17l-5.8 3.3 1.4-6.4-4.9-4.4 6.5-.7z"/></svg>Favourites
    </div>
  </nav>
</header>

<aside class="filter">
  <div class="filter-title">
    <svg width="15" height="15" viewBox="0 0 24 24" fill="none" stroke="#fff" stroke-width="2"><rect x="2" y="3" width="20" height="8" rx="4"/><rect x="2" y="13" width="20" height="8" rx="4"/></svg>Filter
  </div>
  <div class="dark-toggle">
    <svg width="12" height="12" viewBox="0 0 24 24" fill="none" stroke="#1b2c3e" stroke-width="2"><path d="M20 14A8 8 0 1 1 10 4a7 7 0 0 0 10 10z"/></svg>Dark mode
  </div>

  <div class="f-label" style="top:72px">Sector:</div>
  <div class="f-input" style="left:94px;top:67px;width:187px;padding:0 13px">Ex: Materials</div>

  <div class="f-label" style="top:111px">Time:</div>
  <div class="f-text" style="left:93px;top:113px">From</div>
  <svg class="cal" style="left:129px;top:114px" viewBox="0 0 12 12" fill="none" stroke="#6fa4d4"><rect x="1" y="2" width="10" height="9"/><path d="M1 5h10M4 1v2M8 1v2"/></svg>
  <div class="f-text" style="left:161px;top:113px">To</div>
  <svg class="cal" style="left:182px;top:114px" viewBox="0 0 12 12" fill="none" stroke="#6fa4d4"><rect x="1" y="2" width="10" height="9"/><path d="M1 5h10M4 1v2M8 1v2"/></svg>

  <div class="f-label" style="top:152px">Quality:</div>
  <div class="f-text" style="left:93px;top:154px">From</div>
  <div class="f-input" style="left:129px;top:147px;width:60px">Ex: 1.2</div>
  <div class="f-text" style="left:200px;top:154px">To</div>
  <div class="f-input" style="left:221px;top:147px;width:60px">Ex: 40.00</div>

  <div class="f-label" style="top:192px">Stat:</div>
  <div class="f-text" style="left:93px;top:194px">From</div>
  <div class="f-input" style="left:129px;top:186px;width:60px">Ex: 1.2</div>
  <div class="f-text" style="left:200px;top:194px">To</div>
  <div class="f-input" style="left:221px;top:186px;width:60px">Ex: 40.00</div>

  <div class="cancel">Cancel</div>
  <div class="apply">Apply</div>
</aside>

<div class="asset-tab active" style="left:335px">EQUITIES</div>
<div class="asset-tab" style="left:449px">ETFS</div>
<div class="asset-tab" style="left:524px">PAIRS</div>
<div class="asset-tab" style="left:604px">ETF PAIRS</div>
<div class="asset-tab" style="left:708px">FACTORS</div>
<svg class="popout" viewBox="0 0 14 14" fill="none" stroke="#2b8be0" stroke-width="1.6"><path d="M11 8v4H2V3h4M8 2h4v4M12 2 6 8"/></svg>

<section class="models">
  <div class="row head">
    <span class="id-cell">ID <svg width="8" height="6" viewBox="0 0 8 6" fill="none" stroke="#8d96a0" stroke-width="1.3"><path d="m1 1.5 3 3 3-3"/></svg></span>
    <span>Sector</span><span>Time</span><span>Quality</span><span>Stat 1</span><span>Stat 2</span><span>Stat 3</span><span>Stat 4</span><span>Stat 5</span><span>Stat 6</span><span>Stat 7</span><span>Stat 8</span>
  </div>
  <div class="row body">
    <span class="id-cell"><svg class="star" viewBox="0 0 24 24" fill="none" stroke="#b9c0c8" stroke-width="2"><path d="m12 2.8 2.8 6 6.5.7-4.9 4.4 1.4 6.4L12 17l-5.8 3.3 1.4-6.4-4.9-4.4 6.5-.7z"/></svg>Model 1</span>
    <span>Materials</span><span class="time">2019-07-03<br>12:15:00.000</span><span>30.2888</span><span>2.01574</span><span>23.305</span><span>-0.149368</span><span>22.3054</span><span>4.63714</span><span>0.945706</span><span>2.81949</span><span>2.608</span>
  </div>
  <div class="row body">
    <span class="id-cell"><svg class="star" viewBox="0 0 24 24" fill="#e8473f"><path d="m12 2.8 2.8 6 6.5.7-4.9 4.4 1.4 6.4L12 17l-5.8 3.3 1.4-6.4-4.9-4.4 6.5-.7z"/></svg>Model 2</span>
    <span>Materials</span><span class="time">2019-07-03<br>12:15:00.000</span><span>30.2888</span><span>2.01574</span><span>23.305</span><span>-0.149368</span><span>22.3054</span><span>4.63714</span><span>0.945706</span><span>2.81949</span><span>2.608</span>
  </div>
  <div class="row body">
    <span class="id-cell"><svg class="star" viewBox="0 0 24 24" fill="none" stroke="#b9c0c8" stroke-width="2"><path d="m12 2.8 2.8 6 6.5.7-4.9 4.4 1.4 6.4L12 17l-5.8 3.3 1.4-6.4-4.9-4.4 6.5-.7z"/></svg>Model 3</span>
    <span>Materials</span><span class="time">2019-07-03<br>12:15:00.000</span><span>30.2888</span><span>2.01574</span><span>23.305</span><span>-0.149368</span><span>22.3054</span><span>4.63714</span><span>0.945706</span><span>2.81949</span><span>2.608</span>
  </div>
  <div class="row body">
    <span class="id-cell"><svg class="star" viewBox="0 0 24 24" fill="none" stroke="#b9c0c8" stroke-width="2"><path d="m12 2.8 2.8 6 6.5.7-4.9 4.4 1.4 6.4L12 17l-5.8 3.3 1.4-6.4-4.9-4.4 6.5-.7z"/></svg>Model 4</span>
    <span>Materials</span><span class="time">2019-07-03<br>12:15:00.000</span><span>30.2888</span><span>2.01574</span><span>23.305</span><span>-0.149368</span><span>22.3054</span><span>4.63714</span><span>0.945706</span><span>2.81949</span><span>2.608</span>
  </div>
  <div class="row body">
    <span class="id-cell"><svg class="star" viewBox="0 0 24 24" fill="none" stroke="#b9c0c8" stroke-width="2"><path d="m12 2.8 2.8 6 6.5.7-4.9 4.4 1.4 6.4L12 17l-5.8 3.3 1.4-6.4-4.9-4.4 6.5-.7z"/></svg>Model 5</span>
    <span>Materials</span><span class="time">2019-07-03<br>12:15:00.000</span><span>30.2888</span><span>2.01574</span><span>23.305</span><span>-0.149368</span><span>22.3054</span><span>4.63714</span><span>0.945706</span><span>2.81949</span><span>2.608</span>
  </div>
  <div class="row body">
    <span class="id-cell"><svg class="star" viewBox="0 0 24 24" fill="none" stroke="#b9c0c8" stroke-width="2"><path d="m12 2.8 2.8 6 6.5.7-4.9 4.4 1.4 6.4L12 17l-5.8 3.3 1.4-6.4-4.9-4.4 6.5-.7z"/></svg>Model 6</span>
    <span>Materials</span><span class="time">2019-07-03<br>12:15:00.000</span><span>30.2888</span><span>2.01574</span><span>23.305</span><span>-0.149368</span><span>22.3054</span><span>4.63714</span><span>0.945706</span><span>2.81949</span><span>2.608</span>
  </div>
</section>
</body>
</html>
```